Letterhead Design for Law Firm

**Edit: I have added the photo of a bottom that I like.

------
We are looking for a re-design of our new letterhead. The letterhead is for a law firm and will be used for digital and traditionally printed correspondence.

Here are some suggestions:

- Please use colours are #8ec900 and simple black.
- Please do not use any type of "waves" at the bottom of the page. This is not in style at all.
- Please stay modern yet conservative.
- Please use font Segoe UI Light or similar if you can
- Avoid clipart or illustrations.
- Utilize ample white space in the layout so the design looks clean and information is easy to read at a glance. Don't overcrowd the letterhead.
- Make sure the letterhead design is consistent with our brand identity (see brambleford.ca)
-Please, no black headers or footers.

I am attaching my current letterhead and signature for your convenience.

Remember, the letterhead is an extension of our professional identity. We are a successful firm and trial lawyers who correspond with insurers, judges, lawyers, courts, clients, etc. Make it new, modern, attractive, yet powerful and conservative.

It needs to be easily printable. I would like the bleed removed in print so the black bar the bottom crosses the page (but the text is not near the edges)

Target Market(s)

Clients, Government Offices, Judiciary, Lawyers, Insurance Companies, Colleagues.

Industry/Entity Type

Law

Font styles to use
Other font styles liked:
• Segoe UI LIght, Calibri Light,

Colors
00AB8E
00BBA5
67D7C9
C6EFE9
E9F9F6

Requirements
Must have
• Everything that is on the letterhead now.
Nice to have
• Cutting Edge design, yet conservative.
Should not have
• law firm cliche design, images,

```html
<!DOCTYPE html>
<html lang="en">
<head>
<meta charset="utf-8">
<title>Corbett Personal Injury Lawyers – Letterhead</title>
<link rel="stylesheet" href="https://fonts.googleapis.com/css2?family=Open+Sans:wght@300;400;600&display=swap">
<style>
  :root {
    --brand-green: #8ec900;
    --ink: #000000;
    --text-grey: #444444;
    --paper: #ffffff;
    --backdrop: #e6e7e8;
  }
  * { box-sizing: border-box; margin: 0; padding: 0; }
  html, body {
    width: 1200px; height: 1200px; overflow: hidden;
    background: var(--backdrop);
    font-family: "Open Sans", "Segoe UI", sans-serif;
  }
  .letterhead {
    position: absolute; left: 366px; top: 197px;
    width: 689px; height: 891px;
    background: var(--paper);
    box-shadow: 0 2px 10px rgba(0,0,0,0.12);
  }
  .bar { position: absolute; }
  .bar--top-black { left: 0; top: 0; width: 231px; height: 6px; background: var(--ink); }
  .bar--left-green { left: 0; top: 6px; width: 6px; height: 299px; background: var(--brand-green); }
  .bar--right-black { right: 0; top: 586px; width: 7px; height: 299px; background: var(--ink); }
  .bar--bottom-green { right: 0; bottom: 0; width: 231px; height: 6px; background: var(--brand-green); }

  .firm-name {
    position: absolute; left: 26px; top: 26px;
    color: var(--ink); font-weight: 400;
  }
  .firm-name__main { display: block; font-size: 46px; line-height: 48px; letter-spacing: 0.5px; }
  .firm-name__sub { display: block; font-size: 12px; letter-spacing: 1.9px; margin-top: 4px; }

  .closing {
    position: absolute; left: 62px; top: 686px;
    font-size: 10.5px; line-height: 13.5px; font-weight: 600; color: var(--text-grey);
  }
  .closing__signature {
    width: 180px; height: 36px; margin: 6px 0 14px;
    background: linear-gradient(90deg, #f4f4f4, #e2e2e2);
  }

  .contact {
    position: absolute; right: 24px; top: 600px;
    text-align: right; font-weight: 300; font-style: normal; font-size: 12.5px; color: var(--text-grey);
  }
  .contact__line { display: flex; justify-content: flex-end; align-items: center; gap: 5px; height: 19.5px; }
  .contact__line--plain { height: 15px; padding-right: 17px; }
  .contact__icon { width: 12px; height: 12px; fill: var(--brand-green); flex: none; }
  .contact__clerk { margin-top: 4px; padding-right: 2px; }
  .contact__clerk-label { color: var(--brand-green); font-weight: 400; }

  .practice {
    position: absolute; right: 24px; top: 759px;
    text-align: right; font-weight: 300; font-size: 12.5px; color: var(--text-grey);
  }
  .practice__title { color: var(--brand-green); font-weight: 400; font-size: 12.5px; height: 20px; }
  .practice__item { display: flex; justify-content: flex-end; align-items: center; gap: 5px; height: 18.5px; }
  .practice__diamond { width: 7px; height: 7px; background: var(--brand-green); transform: rotate(45deg); margin: 0 1px 0 2px; }
</style>
</head>
<body>
  <main class="letterhead">
    <div class="bar bar--top-black"></div>
    <div class="bar bar--left-green"></div>
    <div class="bar bar--right-black"></div>
    <div class="bar bar--bottom-green"></div>

    <header class="firm-name">
      <span class="firm-name__main">CORBETT</span>
      <span class="firm-name__sub">PERSONAL INJURY LAWYERS</span>
    </header>

    <section class="closing">
      <p>Yours Very Truly,</p>
      <p>CORBETT PERSONAL INJURY LAWYERS</p>
      <div class="closing__signature" role="img" aria-label="Handwritten signature of Evan T. Corbett"></div>
      <p>Evan T. Corbett</p>
      <p>Corbett Law Professional Corporation</p>
      <p>/nw</p>
      <p>Encl.</p>
    </section>

    <address class="contact">
      <div class="contact__line">613-555-0142
        <svg class="contact__icon" viewBox="0 0 24 24"><path d="M6.6 10.8a15.1 15.1 0 0 0 6.6 6.6l2.2-2.2c.3-.3.7-.4 1-.2 1.1.4 2.3.6 3.6.6.6 0 1 .4 1 1V20c0 .6-.4 1-1 1A17 17 0 0 1 3 4c0-.6.4-1 1-1h3.5c.6 0 1 .4 1 1 0 1.3.2 2.5.6 3.6.1.3 0 .7-.2 1z"/></svg>
      </div>
      <div class="contact__line">613-555-0187
        <svg class="contact__icon" viewBox="0 0 24 24"><path d="M6 2h12v5H6zM4 8h16a2 2 0 0 1 2 2v7h-4v5H6v-5H2v-7a2 2 0 0 1 2-2zm4 8v4h8v-4z"/></svg>
      </div>
      <div class="contact__line">nora@brambleford.ca
        <svg class="contact__icon" viewBox="0 0 24 24"><path d="M2 5h20v14H2zm2 2v.5l8 5 8-5V7l-8 5z"/></svg>
      </div>
      <div class="contact__line">www.BRAMBLEFORD.ca
        <svg class="contact__icon" viewBox="0 0 24 24"><path d="M12 2a10 10 0 1 0 0 20 10 10 0 0 0 0-20zm6.9 6h-3a15 15 0 0 0-1.3-3.9A8 8 0 0 1 18.9 8zM12 4c.9 1.2 1.6 2.5 2 4h-4c.4-1.5 1.1-2.8 2-4zM4.3 14a8 8 0 0 1 0-4h3.4a16 16 0 0 0 0 4zm.8 2h3a15 15 0 0 0 1.3 3.9A8 8 0 0 1 5.1 16zm3-8h-3a8 8 0 0 1 4.3-3.9C8.8 5.3 8.4 6.6 8.1 8zM12 20c-.9-1.2-1.6-2.5-2-4h4c-.4 1.5-1.1 2.8-2 4zm2.3-6H9.7a14 14 0 0 1 0-4h4.6a14 14 0 0 1 0 4zm.3 5.9c.6-1.2 1-2.5 1.3-3.9h3a8 8 0 0 1-4.3 3.9zm1.7-5.9a16 16 0 0 0 0-4h3.4a8 8 0 0 1 0 4z"/></svg>
      </div>
      <div class="contact__line">48 Harbour Street W., Suite 1210
        <svg class="contact__icon" viewBox="0 0 24 24"><path d="M12 2a7 7 0 0 0-7 7c0 5.3 7 13 7 13s7-7.7 7-13a7 7 0 0 0-7-7zm0 9.5a2.5 2.5 0 1 1 0-5 2.5 2.5 0 0 1 0 5z"/></svg>
      </div>
      <div class="contact__line contact__line--plain">Ashbury, ON&nbsp; K2R 3K2</div>
      <p class="contact__clerk"><span class="contact__clerk-label">File Clerk:</span> Nora Whitfield</p>
    </address>

    <section class="practice">
      <h2 class="practice__title">PRACTICE RESTRICTED</h2>
      <div class="practice__item">Serious Personal Injury <span class="practice__diamond"></span></div>
      <div class="practice__item">Wrongful Death Litigation <span class="practice__diamond"></span></div>
      <div class="practice__item">Long-Term Disability Litigation <span class="practice__diamond"></span></div>
      <div class="practice__item">Wrongful Dismissal Litigation <span class="practice__diamond"></span></div>
      <div class="practice__item">Employee Terminations <span class="practice__diamond"></span></div>
    </section>
  </main>
</body>
</html>
```